Industrial Automation company requires a business card design

Valtrin Automation provides design & build of Automated Equipment for manufacturing industry.
www.valtrinautomation.example
The equipment we design is used for manufacturing in sectors such as medical device, pharmaceutical, aerospace and electronics.
We require a new business card design which incorporates our (New) logo and the key message words:
Automated Equipment:
Design, Build, Control, Test, Support

```html
<!DOCTYPE html>
<html lang="en">
<head>
<meta charset="utf-8">
<title>Valtrin Automation – Business Card</title>
<link rel="stylesheet" href="https://fonts.googleapis.com/css2?family=Lato:wght@400;700;900&display=swap">
<style>
  :root {
    --bg: #1b1b1b;
    --green: #0a7d41;
    --black: #231f20;
    --white: #ffffff;
    --grey-text: #d9d9d9;
  }
  * { box-sizing: border-box; margin: 0; padding: 0; }
  html, body { width: 1200px; height: 800px; overflow: hidden; }
  body {
    background: var(--bg);
    font-family: "Lato", Arial, sans-serif;
    display: flex;
    align-items: center;
    justify-content: center;
    gap: 40px;
  }
  .card {
    width: 540px;
    height: 309px;
    position: relative;
    overflow: hidden;
    border-radius: 3px;
    box-shadow: 0 10px 30px rgba(0,0,0,.5);
  }

  /* Front */
  .card-front {
    background: var(--green);
    color: var(--white);
    display: flex;
    flex-direction: column;
    align-items: center;
    justify-content: center;
  }
  .wordmark {
    display: flex;
    align-items: center;
    gap: 14px;
    font-weight: 900;
    letter-spacing: 3px;
    text-transform: uppercase;
  }
  .wordmark-dot {
    width: 34px; height: 34px; border-radius: 50%;
  }
  .card-front .wordmark { font-size: 34px; color: var(--white); }
  .card-front .wordmark-dot { background: var(--white); }
  .front-url {
    margin-top: 54px;
    font-size: 15px;
    font-weight: 700;
    letter-spacing: .3px;
  }

  /* Back */
  .card-back { background: var(--white); }
  .back-logo-zone {
    height: 46%;
    display: flex;
    align-items: center;
    justify-content: center;
  }
  .card-back .wordmark { font-size: 30px; color: var(--green); }
  .card-back .wordmark-dot { background: var(--green); width: 30px; height: 30px; }
  .back-info-band {
    height: 36%;
    background: var(--green);
    color: var(--white);
    display: flex;
    align-items: center;
    padding: 0 26px;
  }
  .person {
    width: 185px;
    text-align: right;
    padding-right: 18px;
  }
  .person-name { font-size: 16px; font-weight: 700; letter-spacing: .3px; }
  .person-title { font-size: 10px; text-transform: uppercase; margin-top: 2px; letter-spacing: .3px; }
  .divider { width: 1px; height: 76px; background: var(--white); }
  .contacts {
    list-style: none;
    padding-left: 18px;
    font-size: 12.5px;
    line-height: 1.45;
  }
  .contacts li { display: flex; align-items: center; gap: 8px; }
  .contacts svg { width: 11px; height: 11px; fill: var(--white); flex: none; }
  .back-tagline-strip {
    height: 18%;
    background: var(--black);
    color: var(--white);
    display: flex;
    align-items: center;
    padding-left: 26px;
    font-size: 12px;
    letter-spacing: .4px;
    text-transform: uppercase;
  }
</style>
</head>
<body>

  <section class="card card-front" aria-label="Business card front">
    <div class="wordmark"><span class="wordmark-dot"></span>Valtrin Automation</div>
    <div class="front-url">www.valtrinautomation.example</div>
  </section>

  <section class="card card-back" aria-label="Business card back">
    <div class="back-logo-zone">
      <div class="wordmark"><span class="wordmark-dot"></span>Valtrin Automation</div>
    </div>
    <div class="back-info-band">
      <div class="person">
        <div class="person-name">MARCUS HALE</div>
        <div class="person-title">Director Operations</div>
      </div>
      <div class="divider"></div>
      <ul class="contacts">
        <li><svg viewBox="0 0 24 24"><path d="M6.6 10.8a15 15 0 0 0 6.6 6.6l2.2-2.2c.3-.3.7-.4 1-.2 1.1.4 2.3.6 3.6.6.6 0 1 .4 1 1V20c0 .6-.4 1-1 1A17 17 0 0 1 3 4c0-.6.4-1 1-1h3.5c.6 0 1 .4 1 1 0 1.3.2 2.5.6 3.6.1.3 0 .7-.2 1z"/></svg>1555-0142-7788</li>
        <li><svg viewBox="0 0 24 24"><path d="M7 1h10a2 2 0 0 1 2 2v18a2 2 0 0 1-2 2H7a2 2 0 0 1-2-2V3a2 2 0 0 1 2-2zm0 3v14h10V4zm5 15.5a1 1 0 1 0 0 2 1 1 0 0 0 0-2z"/></svg>0455-0190-2234</li>
        <li><svg viewBox="0 0 24 24"><path d="M2 4h20v16H2zm2 2v.5l8 5 8-5V6zm0 3v9h16V9l-8 5z"/></svg>marcus.hale@valtrin.example</li>
        <li><svg viewBox="0 0 24 24"><path d="M12 2a10 10 0 1 0 0 20 10 10 0 0 0 0-20zm6.9 6h-3a15 15 0 0 0-1.3-3.9A8 8 0 0 1 18.9 8zM12 4c.8 1.2 1.5 2.5 1.9 4h-3.8c.4-1.5 1.1-2.8 1.9-4zM4.3 14a8 8 0 0 1 0-4h3.4a16 16 0 0 0 0 4zm.8 2h3a15 15 0 0 0 1.3 3.9A8 8 0 0 1 5.1 16zm3-8h-3a8 8 0 0 1 4.3-3.9C8.8 5.3 8.4 6.6 8.1 8zM12 20c-.8-1.2-1.5-2.5-1.9-4h3.8c-.4 1.5-1.1 2.8-1.9 4zm2.3-6H9.7a14 14 0 0 1 0-4h4.6a14 14 0 0 1 0 4zm.3 5.9c.6-1.2 1-2.5 1.3-3.9h3a8 8 0 0 1-4.3 3.9zm1.7-5.9a16 16 0 0 0 0-4h3.4a8 8 0 0 1 0 4z"/></svg>www.valtrinautomation.example</li>
      </ul>
    </div>
    <div class="back-tagline-strip">Design | Build | Control | Test | Support</div>
  </section>

</body>
</html>
```